Tech Startup Needs Business Card Design

I am looking for an eye catching business card design for our new company, Torn Kite. We are a place for business owners and contractors to share their experiences with their customers and check their current customers. Our website, www.torn-kite.co, may be able to offer some guidance as to the design.

Industry/Entity Type

Business

Contact Information for Business Card

Owen Barthwick
888-417-3083
Owen@torn-kite.co
www.torn-kite.co

```html
<!DOCTYPE html>
<html lang="en">
<head>
<meta charset="utf-8">
<title>Torn Kite — Business Card</title>
<link href="https://fonts.googleapis.com/css2?family=Varela+Round&display=swap" rel="stylesheet">
<style>
  :root {
    --canvas: #ecebe8;
    --brand-red: #e5312e;
    --box-red: #ee1f26;
    --ink: #333333;
    --muted: #6b6b6b;
    --paper: #ffffff;
    --leaf: #3aa640;
    --shadow: rgba(0, 0, 0, 0.18);
  }
  * { margin: 0; padding: 0; box-sizing: border-box; }
  html, body {
    width: 1200px;
    height: 1023px;
    overflow: hidden;
    background: var(--canvas);
    font-family: "Varela Round", "Arial Rounded MT Bold", sans-serif;
  }
  .sheet {
    position: relative;
    width: 1200px;
    height: 1023px;
    display: flex;
    flex-direction: column;
    align-items: center;
    justify-content: center;
    gap: 64px;
  }
  .card {
    position: relative;
    width: 700px;
    height: 400px;
    border-radius: 4px;
    box-shadow: 0 10px 30px var(--shadow);
    overflow: hidden;
  }
  .card--front {
    background: var(--brand-red);
    display: flex;
    align-items: center;
    justify-content: center;
  }
  .wordmark {
    display: flex;
    align-items: center;
    gap: 18px;
  }
  .wordmark__dot {
    width: 26px;
    height: 26px;
    border-radius: 50%;
    background: var(--leaf);
  }
  .wordmark__name {
    color: var(--paper);
    font-size: 104px;
    line-height: 1;
    letter-spacing: -1px;
    white-space: nowrap;
  }
  .card--back {
    background: var(--paper);
  }
  .card--back .wordmark {
    position: absolute;
    top: 34px;
    left: 38px;
    gap: 8px;
  }
  .card--back .wordmark__dot {
    width: 10px;
    height: 10px;
  }
  .card--back .wordmark__name {
    color: var(--brand-red);
    font-size: 30px;
    letter-spacing: 0;
  }
  .contact {
    position: absolute;
    left: 38px;
    bottom: 70px;
    width: 200px;
    list-style: none;
    display: flex;
    flex-direction: column;
    gap: 12px;
  }
  .contact__item {
    display: flex;
    align-items: center;
    gap: 10px;
    color: var(--muted);
    font-size: 15px;
    line-height: 1.2;
    white-space: nowrap;
  }
  .contact__icon {
    width: 16px;
    height: 16px;
    flex: none;
    fill: none;
    stroke: var(--brand-red);
    stroke-width: 1.8;
    stroke-linecap: round;
    stroke-linejoin: round;
  }
  .name-panel {
    position: absolute;
    right: 0;
    bottom: 70px;
    width: 430px;
    height: 150px;
    background: var(--box-red);
    border-radius: 22px 0 0 22px;
    padding: 36px 40px;
  }
  .name-panel__name {
    color: var(--ink);
    font-size: 36px;
    font-weight: 700;
    line-height: 1.1;
    white-space: nowrap;
  }
  .name-panel__title {
    margin-top: 10px;
    color: rgba(255, 255, 255, 0.8);
    font-size: 18px;
    letter-spacing: 2px;
  }
</style>
</head>
<body>
  <main class="sheet">
    <section class="card card--front" aria-label="Card front">
      <div class="wordmark">
        <span class="wordmark__dot"></span>
        <span class="wordmark__name">Torn Kite</span>
      </div>
    </section>

    <section class="card card--back" aria-label="Card back">
      <div class="wordmark">
        <span class="wordmark__dot"></span>
        <span class="wordmark__name">Torn Kite</span>
      </div>

      <ul class="contact">
        <li class="contact__item">
          <svg class="contact__icon" viewBox="0 0 16 16" aria-hidden="true"><path d="M3 2h3l1.5 3.5-2 1.2a8 8 0 0 0 3.8 3.8l1.2-2L14 10v3a1 1 0 0 1-1 1A11 11 0 0 1 2 3a1 1 0 0 1 1-1z"/></svg>
          <span>888-417-3083</span>
        </li>
        <li class="contact__item">
          <svg class="contact__icon" viewBox="0 0 16 16" aria-hidden="true"><rect x="1.5" y="3.5" width="13" height="9" rx="1.5"/><path d="M2 4.5l6 4.5 6-4.5"/></svg>
          <span>Owen@torn-kite.co</span>
        </li>
        <li class="contact__item">
          <svg class="contact__icon" viewBox="0 0 16 16" aria-hidden="true"><circle cx="8" cy="8" r="6.5"/><path d="M1.5 8h13M8 1.5c2 2 2 11 0 13M8 1.5c-2 2-2 11 0 13"/></svg>
          <span>www.torn-kite.co</span>
        </li>
      </ul>

      <div class="name-panel">
        <p class="name-panel__name">Owen Barthwick</p>
        <p class="name-panel__title">CEO</p>
      </div>
    </section>
  </main>
</body>
</html>
```